ONE PAGE WEBSITE for Cool Recruitment Agency

Hello creative gurus,

We're are after a ONE PAGE World Press web design.

We're a recruitment start-up specializing in Information Technology.

The design should be cool, quirky and NOT mainstream.

The kind of web designs we like:

http://www.brivontek.co.za/#what-we-do
http://foldthelantern.com/
http://www.kelzo.com/index.html#home
http://marekvillandro.com/#/selected-works

And, we only like the front page of this web site: http://www.dunbywhim.com/

Any questions, please do let us know!

Thank you, and happy creating!

Dara
Updates

Reason: Just need a day or two to finalize everything. Thanks, Dara

Target Market(s)

Companies, employees, candidates

Industry/Entity Type

Recruitment

Coding

Coded - Design and coding required

Colors
f37122
f68e4e
ffcf3e
00a990
86cfc6
fcca95
fee18a

Requirements
Must have
• 1. The website should be techy, cool, funky, quirky and user-friendly.
• 2. Mobile-compatible
• 3. Please use our spaceman logo through the website (attached).
• 4. Please see attached website content/brief.
• 5. Colors - orange color is a must, but please use other colors to spice it up - make it more fun.
• The kind of web designs we like:
• http://www.brivontek.co.za/#what-we-do
• http://foldthelantern.com/
• http://www.kelzo.com/index.html#home
• http://marekvillandro.com/#/selected-works
• http://www.dunbywhim.com/
• Any questions, please do let us know!
Should not have
• -NO stock image banners, photos, images

```html
<!DOCTYPE html>
<html lang="en">
<head>
<meta charset="utf-8">
<title>Kovalo – Contact Us</title>
<link rel="stylesheet" href="https://fonts.googleapis.com/css2?family=Lato:wght@400;700&family=Roboto:wght@500;700&display=swap">
<style>
:root{
  --orange:#f37122;
  --orange-light:#f68e4e;
  --teal:#00a990;
  --ink:#2b2b2b;
  --sidebar:#eeeeee;
  --main:#e9e9e9;
  --nav:#dcdcdc;
  --field:#ffffff;
  --field-border:#d6d6d6;
  --map-water:#9cc6ee;
  --map-land:#ece6da;
}
*{box-sizing:border-box;margin:0;padding:0}
html,body{width:1200px;height:1200px;overflow:hidden;background:#fff}
body{font-family:'Lato',sans-serif;color:var(--ink);position:relative}
.page{position:absolute;left:82px;top:0;width:1036px;height:1200px;background:var(--main);overflow:hidden}
.page-deco{position:absolute;border-radius:50%;background:rgba(255,255,255,.25)}
.sidebar{position:absolute;left:0;top:0;width:266px;height:1200px;background:var(--sidebar)}
.brand{position:absolute;left:12px;top:20px;display:flex;align-items:center}
.brand-dot{width:60px;height:60px;border-radius:50%;background:#1f1f1f}
.brand-name{margin-left:8px;margin-top:22px;font-family:'Roboto',sans-serif;font-weight:700;font-size:30px;letter-spacing:2px;color:var(--orange);white-space:nowrap}
.tagline{position:absolute;left:75px;top:91px;font-family:'Roboto',sans-serif;font-weight:500;font-size:11px;color:#222;white-space:nowrap}
.nav{position:absolute;left:11px;top:126px;width:243px;list-style:none}
.nav li{height:38px;margin-bottom:7.6px;background:var(--nav);border-radius:3px;display:flex;align-items:center;justify-content:center;font-family:'Roboto',sans-serif;font-weight:500;font-size:14px;color:#222;white-space:nowrap}
.nav li.active{background:linear-gradient(var(--orange-light),var(--orange));color:#fff}
.follow{position:absolute;left:15px;top:1076px;font-weight:700;font-size:19px;color:#333;white-space:nowrap}
.social{position:absolute;left:15px;top:1109px;display:flex;gap:10px}
.social span{width:28px;height:28px;background:#d3d3d3}
.social span.first{background:var(--orange)}
.copyright{position:absolute;left:15px;top:1152px;font-weight:700;font-size:10.5px;color:#333;white-space:nowrap}
.content{position:absolute;left:0;top:0}
.title{position:absolute;left:292px;top:44px;font-family:'Roboto',sans-serif;font-weight:700;font-size:29px;color:var(--teal);white-space:nowrap}
.lead{position:absolute;left:294px;font-weight:700;font-size:17px;white-space:nowrap;color:#2a2a2a}
.map{position:absolute;left:290px;top:170px;width:722px;height:267px;background:linear-gradient(90deg,var(--map-water) 0%,var(--map-land) 25%,var(--map-land) 70%,var(--map-water) 100%)}
.cta{position:absolute;top:468px;height:31px;width:199px;display:flex;align-items:center;justify-content:center;color:#fff;font-weight:700;white-space:nowrap}
.cta-mail{left:450px;background:var(--teal);font-size:15px;text-decoration:underline}
.cta-call{left:654px;background:var(--orange);font-size:18px}
.label{position:absolute;font-weight:700;font-size:14px;line-height:18px;color:#2a2a2a;white-space:nowrap}
.field{position:absolute;background:var(--field);border:1px solid var(--field-border)}
.submit{position:absolute;left:291px;top:845px;width:151px;height:37px;background:var(--teal);color:#fff;font-weight:700;font-size:14px;display:flex;align-items:center;justify-content:center;white-space:nowrap}
</style>
</head>
<body>
<div class="page">
  <div class="page-deco" style="left:600px;top:-100px;width:600px;height:600px"></div>
  <div class="page-deco" style="left:600px;top:900px;width:500px;height:500px"></div>

  <aside class="sidebar">
    <div class="brand"><div class="brand-dot"></div><div class="brand-name">KOVALO</div></div>
    <div class="tagline">Helping Talent &amp; Company Connets</div>
    <ul class="nav">
      <li class="active">HOME</li>
      <li>ABOUT US</li>
      <li>COMPANIES</li>
      <li>TALENT</li>
      <li>REFERALS</li>
      <li>BLOG</li>
      <li>CONTACT US</li>
    </ul>
    <div class="follow">Follow Us:</div>
    <div class="social"><span class="first"></span><span></span><span></span><span></span></div>
    <div class="copyright">© 2017 kovalotalent.com</div>
  </aside>

  <main class="content">
    <h1 class="title">CONTACT US</h1>
    <p class="lead" style="top:89px">If you'd like to discover more about how we work, then please do get in touch.</p>
    <p class="lead" style="top:123px">We’re a friendly bunch and we’d be happy to chat to you about working together!</p>
    <div class="map" role="img" aria-label="Street map of the city centre and harbour showing the office location"></div>
    <div class="cta cta-mail">info@kovalotalent.com</div>
    <div class="cta cta-call">Call Us 0288 513207</div>

    <div class="label" style="left:292px;top:539px">First Name:</div>
    <div class="label" style="left:663px;top:539px">Last Name:</div>
    <div class="field" style="left:291px;top:566px;width:349px;height:29px"></div>
    <div class="field" style="left:662px;top:566px;width:349px;height:29px"></div>
    <div class="label" style="left:292px;top:607px">Email:</div>
    <div class="label" style="left:663px;top:607px">Mobile Number:</div>
    <div class="field" style="left:291px;top:634px;width:349px;height:30px"></div>
    <div class="field" style="left:662px;top:634px;width:349px;height:30px"></div>
    <div class="label" style="left:293px;top:675px">Your Message:</div>
    <div class="field" style="left:291px;top:702px;width:721px;height:126px"></div>
    <div class="submit">Submit Here</div>
  </main>
</div>
</body>
</html>
```